Wordpress Design Project - Australian Solar Company wants to start FRESH!

About us

Bright Meadow are a renewable energy company based in Perth Australia, but we also have offices all over Asia. We specialise in offering renewable energy solutions (Solar PV Systems and LED Lighting) to residential and commercial customers.

Our current website: www.brightmeadowenergy.com.au

Our needs

This will be a replacement website as we are not happy with our current layout. We have an Australian company doing our SEO and they have recommended a new layout which we wish to go with.

We really want a professional and easy to navigate website that will assist in bringing in more enquiries and phone calls.

Content

We have all the content and will get the design winner to add this after we have chosen the design we like.
It is important that the call to actions are presented well and are visible these are things like the free quote form and our phone number.

The layout as we have advised has been based on SEO research so we wish it to be exactly the same unless otherwise stated.

Call to action

Our main objective of the new website is for people to come to the home page and see us as a professional and reliable company to deal with and enquire further.

We really want as many people as we can to convert to a lead. We want every person that comes to the website to enquire online or call us. We feel it is important to have a contact us/quote form on every page of the website.

Functional requirements

We have a chatterbook and vidstream account so links to these would be needed

Design assets

The logo needs to be displayed as shown in the website layout brief

Colours – we would like fresh, subdued colours that are professional and appealing to the eye. We ask that you do not take the colours from the logo.

Current website dislikes – the things we currently dislike about our current website is that it is hard to find information and there is no clear call to action. The colours are really unappealing as well as it looks cheap not professional.
The graphics that we require for the slider on the home page will have to be given after the winner is chosen but we want there to be three sliders on rotation

- Credibility builder (employee infront of solar panel) that encourages we use all our own employees not subcontractors
- Residential Slider – picture of a couple and solar panel system with a testimonial
- Commercial slider – picture of commercial system with “find out how you can install solar for free* at your business”

Design ideas

The website needs to be mobile friendly as well
It is going to be a total rebuild from the current website as our current website really isn’t working for us.

Target Market(s)

Target Audience

Our target audience are both residential and commercial clients
Residential – we want to attract home owners that are interested in reducing their electricity bill and helping the environment. Generally these people are between the ages of 28-50+ both male and female.

Commercial – We want to appeal to key decision makers within the commercial sphere. For example – CEOs, Company Directors, Operation managers and business owners of any industry. These people will be interested in reducing their electricity bills and creating a clean green image for their business.
Our target audience will generally come to our website to get information and enquire for a quote/ product information.

Industry/Entity Type

Residential

Requirements
Must have
• MUST BE LAID OUT LIKE THIS:

http://www.docuvault.com/doc/849302715/Website-Layout

Must have Enquire Now forms on every page that read:

Name
Phone Number
How did you hear about us
Message

```html
<!DOCTYPE html>
<html lang="en">
<head>
<meta charset="utf-8">
<title>Bright Meadow — Home</title>
<link href="https://fonts.googleapis.com/css2?family=Roboto+Condensed:wght@400;700&family=Open+Sans:ital,wght@0,400;0,600;1,600&display=swap" rel="stylesheet">
<style>
:root{
  --green:#1f9a3a;
  --green-dark:#15782b;
  --ink:#111;
  --text:#666;
  --muted:#888;
  --nav-bg:#e6e6e6;
  --nav-line:#c9c9c9;
  --hero:#1e1e1e;
  --gold:#f5b52a;
  --gold-dark:#d9931a;
  --band:#dcdcdc;
  --field:#ececec;
  --field-line:#b9b9b9;
  --footer:#07090c;
  --white:#fff;
}
*{box-sizing:border-box;margin:0;padding:0}
html,body{width:918px;height:1200px;overflow:hidden;background:var(--white)}
body{position:relative;font-family:"Open Sans",sans-serif;color:var(--text)}
.abs{position:absolute}

/* header */
.site-header{position:absolute;left:0;top:0;width:918px;height:128px;
  background:radial-gradient(circle at 430px 0,#fff6d8 0,#fffdf5 110px,#fff 200px)}
.brand{position:absolute;left:100px;top:38px;display:flex;align-items:center;gap:10px}
.brand-dot{width:34px;height:34px;border-radius:50%;background:var(--green)}
.brand-name{font-family:"Roboto Condensed",sans-serif;font-weight:700;font-size:30px;color:var(--green)}
.call{position:absolute;right:102px;top:12px;text-align:right;font-family:"Roboto Condensed",sans-serif}
.call-label{font-size:26px;font-weight:700;color:var(--ink);display:flex;align-items:center;gap:6px;justify-content:flex-end}
.call-number{font-size:24px;font-weight:700;color:var(--green);margin-top:2px}
.social{position:absolute;right:102px;top:96px;display:flex;gap:4px}
.social span{width:17px;height:17px;background:#7a7a7a;border-radius:2px}
.social span:first-child{background:#4aa3c7}

/* nav */
.main-nav{position:absolute;left:0;top:128px;width:918px;height:39px;background:var(--nav-bg);border-bottom:3px solid var(--nav-line)}
.main-nav ul{list-style:none;display:flex;margin-left:96px;height:36px}
.main-nav li{font-family:"Roboto Condensed",sans-serif;font-size:15px;color:#333;display:flex;align-items:center;justify-content:center;border-right:1px solid var(--nav-line)}
.main-nav li.active{background:var(--green);color:var(--white);border-bottom:3px solid var(--green-dark);height:39px}

/* hero */
.hero{position:absolute;left:0;top:167px;width:918px;height:340px;background:var(--hero);overflow:hidden}
.hero-panel{position:absolute;left:330px;top:0;width:500px;height:330px;
  background:linear-gradient(135deg,#5ea6e6,#2f7fd0 55%,#7bb3e6);transform:skewX(-14deg);transform-origin:bottom;border-right:8px solid #cfd3d6}
.hero-copy{position:absolute;left:100px;top:80px;width:250px;text-align:center;font-family:"Roboto Condensed",sans-serif}
.hero-kicker{color:var(--gold);font-size:24px}
.hero-title{color:var(--white);font-size:50px;font-weight:700;line-height:1;margin-top:2px;margin-left:-16px;margin-right:-16px}
.hero-text{color:#8d8d8d;font-size:15px;line-height:19px;margin-top:14px}
.btn-read{display:inline-block;margin-top:22px;width:72px;height:25px;line-height:25px;font-size:12px;color:#222;
  background:linear-gradient(var(--gold),var(--gold-dark));border-radius:2px;margin-left:-18px}
.clouds{position:absolute;left:0;top:440px;width:918px;height:70px}

/* welcome */
.section-title{font-family:"Roboto Condensed",sans-serif;font-weight:700;font-size:22px;color:var(--ink);text-align:center}
.welcome{position:absolute;left:96px;top:516px;width:726px}
.welcome p{font-size:10px;line-height:16px;text-align:center;color:var(--muted);margin-top:6px}
.projects-head{position:absolute;left:96px;top:654px;width:726px;display:flex;align-items:center;gap:12px}
.projects-head .rule{flex:1;border-top:4px dotted #d8d8d8}
.project{position:absolute;top:704px;width:171px;height:159px;box-shadow:0 8px 8px -6px rgba(0,0,0,.35)}
.project-1{left:96px;background:linear-gradient(#151515,#0d0f14);color:var(--white);text-align:center;font-family:"Roboto Condensed",sans-serif;font-weight:700;font-size:15px;line-height:18px;padding-top:48px}
.project-1 svg{display:block;margin:8px auto 0}
.project-2{left:281px;background:linear-gradient(135deg,#c9582a,#3a3f8a 50%,#b8481e)}
.project-3{left:467px;background:linear-gradient(160deg,#7c8898,#3e4f6a 60%,#8a95a3)}
.project-4{left:652px;background:linear-gradient(#6f8fbf 0,#9fb3cf 35%,#3b4d74 60%,#6d7045)}

/* contact band */
.band{position:absolute;left:0;top:885px;width:918px;height:253px;background:var(--band)}
.col-title{font-family:"Roboto Condensed",sans-serif;font-size:16px;color:var(--ink);position:absolute;top:903px}
.field{position:absolute;width:197px;height:19px;background:var(--field);border:1px solid var(--field-line);font-size:9px;color:#777;padding:3px 8px}
.field.area{height:42px}
.tab-btn{position:absolute;top:1114px;height:24px;width:70px;background:var(--footer);color:var(--gold);font-size:12px;font-weight:600;text-align:center;line-height:26px;clip-path:polygon(10px 0,60px 0,70px 100%,0 100%)}
.testimonial{position:absolute;left:350px;width:218px;font-size:9px;line-height:12.7px;color:#666}
.testimonial .quote-ic{float:left;margin:2px 8px 0 0}
.testimonial cite{display:block;font-style:italic;font-weight:600;color:#222;margin-top:7px}
.divider{position:absolute;left:350px;top:1005px;width:218px;border-top:1px solid #c2c2c2}

/* footer */
.site-footer{position:absolute;left:0;top:1138px;width:918px;height:62px;background:var(--footer);text-align:center;font-size:10px}
.footer-nav{margin-top:12px;color:#ddd}
.footer-nav .on{color:var(--gold)}
.footer-nav i{font-style:normal;color:#666;margin:0 5px}
.copyright{color:#666;margin-top:9px}
</style>
</head>
<body>

<header class="site-header">
  <div class="brand"><span class="brand-dot"></span><span class="brand-name">Bright Meadow</span></div>
  <div class="call">
    <div class="call-label">
      <svg width="22" height="22" viewBox="0 0 24 24"><path d="M6.6 10.8a15 15 0 0 0 6.6 6.6l2.2-2.2c.3-.3.7-.4 1-.2 1.1.4 2.3.6 3.6.6.6 0 1 .4 1 1V20c0 .6-.4 1-1 1A17 17 0 0 1 3 4c0-.6.4-1 1-1h3.5c.6 0 1 .4 1 1 0 1.3.2 2.5.6 3.6.1.3 0 .7-.2 1z" fill="#111"/></svg>
      Call Now</div>
    <div class="call-number">1300 555 014</div>
  </div>
  <div class="social" aria-label="Social links"><span></span><span></span><span></span><span></span><span></span><span></span></div>
</header>

<nav class="main-nav">
  <ul>
    <li class="active" style="width:70px">Home</li>
    <li style="width:71px">About</li>
    <li style="width:82px">Product</li>
    <li style="width:86px">Services</li>
    <li style="width:83px">Projects</li>
    <li style="width:74px">Media</li>
    <li style="width:101px">Information</li>
    <li style="width:82px">Enquiry</li>
    <li style="width:80px;border-right:0">Contact</li>
  </ul>
</nav>

<section class="hero">
  <div class="hero-panel" role="img" aria-label="Large solar panel angled toward the sky"></div>
  <div class="hero-copy">
    <div class="hero-kicker">Solar</div>
    <div class="hero-title">Photovoltaic</div>
    <p class="hero-text">All our home Solar Panels are of high quality with long lifetime guarantees.</p>
    <span class="btn-read">Read more</span>
  </div>
</section>
<svg class="clouds" viewBox="0 0 918 70" preserveAspectRatio="none">
  <g fill="#fff">
    <ellipse cx="40" cy="60" rx="90" ry="56"/>
    <ellipse cx="170" cy="62" rx="90" ry="40"/>
    <ellipse cx="330" cy="62" rx="80" ry="45"/>
    <ellipse cx="470" cy="65" rx="100" ry="50"/>
    <ellipse cx="650" cy="62" rx="100" ry="40"/>
    <ellipse cx="800" cy="60" rx="80" ry="42"/>
    <ellipse cx="900" cy="60" rx="60" ry="56"/>
    <rect x="0" y="55" width="918" height="15"/>
  </g>
</svg>

<section class="welcome">
  <h1 class="section-title">Welcome to Bright Meadow</h1>
  <p>Lorem ipsum dolor sit amet, consectetur adipiscing elit. Mauris adipiscing metus a enim pulvinar scelerisque. Maecenas commodo, purus ac congue interdum, erat felis semper sem, eu facilisis risus odio vitae mi. Pellentesque habitant morbi tristique senectus et netus et malesuada fames ac turpis egestas. Proin turpis augue, tristique in ante ac, varius congue sem. Vivamus fringilla, nisl ac blandit tempus, magna orci posuere lorem, a aliquet neque libero vitae sapien. In hac habitasse platea dictumst. Vestibulum tincidunt molestie pharetra. Vestibulum tristique ipsum elit, nec luctus nisl interdum ac. Vestibulum non adipiscing lorem. Cum sociis natoque penatibus et magnis dis parturient montes, nascetur ridiculus mus. Proin et posuere eros. Suspendisse eu justo vitae lectus</p>
</section>

<div class="projects-head"><span class="rule"></span><h2 class="section-title">Latest Projects</h2><span class="rule"></span></div>
<div class="project project-1">900KW Solar PV Project<br>Residential Feed In
  <svg width="22" height="18" viewBox="0 0 22 18"><rect x="1" y="1" width="20" height="16" fill="none" stroke="#fff" stroke-width="2"/><path d="M3 15l5-6 4 4 3-3 4 5z" fill="#fff"/></svg>
</div>
<div class="project project-2" role="img" aria-label="Solar panels on a terracotta tile roof"></div>
<div class="project project-3" role="img" aria-label="Row of solar panels on a sloped roof"></div>
<div class="project project-4" role="img" aria-label="Ground-mounted solar array in a field"></div>

<section class="band"></section>
<h3 class="col-title" style="left:96px">Request quote</h3>
<div class="field" style="left:96px;top:933px">Name :</div>
<div class="field" style="left:96px;top:958px">Company :</div>
<div class="field" style="left:96px;top:983px">Phone number :</div>
<div class="field" style="left:96px;top:1008px">Email Address :</div>
<div class="field" style="left:96px;top:1033px">Website Address :</div>
<div class="field area" style="left:96px;top:1058px">Your Message here :</div>
<div class="tab-btn" style="left:160px">Send</div>

<h3 class="col-title" style="left:350px">Testimonials</h3>
<div class="testimonial" style="top:929px">
  <svg class="quote-ic" width="22" height="16" viewBox="0 0 22 16"><ellipse cx="8" cy="6" rx="8" ry="5.5" fill="#aaa"/><ellipse cx="15" cy="10" rx="7" ry="5" fill="#bbb"/></svg>
  Lorem ipsum dolor sit amet, consectetur adipiscing elit. Integer molestie quam a Lorem ipsum dolor sit amet, consectetur adipiscing elit. Integer molestie quam a magna iaculis
  <cite>Customer Name</cite>
</div>
<div class="divider"></div>
<div class="testimonial" style="top:1014px">
  <svg class="quote-ic" width="22" height="16" viewBox="0 0 22 16"><ellipse cx="8" cy="6" rx="8" ry="5.5" fill="#aaa"/><ellipse cx="15" cy="10" rx="7" ry="5" fill="#bbb"/></svg>
  Lorem ipsum dolor sit amet, consectetur adipiscing elit. Integer molestie quam a Lorem ipsum dolor sit amet, consectetur adipiscing elit. Integer molestie quam a magna iaculis
  <cite>Customer Name</cite>
</div>

<h3 class="col-title" style="left:625px">Contact Us</h3>
<div class="field" style="left:625px;top:933px">Name :</div>
<div class="field" style="left:625px;top:962px">Email :</div>
<div class="field" style="left:625px;top:992px">Phone :</div>
<div class="field area" style="left:625px;top:1022px;height:58px">Message :</div>
<div class="tab-btn" style="left:686px;width:78px;clip-path:polygon(10px 0,68px 0,78px 100%,0 100%)">Submit</div>

<footer class="site-footer">
  <div class="footer-nav"><span class="on">Home</span><i>/</i>About Us<i>/</i>Product<i>/</i>Services<i>/</i>Projects<i>/</i>Media<i>/</i>Information<i>/</i>Enquiry<i>/</i>Contact us</div>
  <div class="copyright">Copyright © 2013 Bright Meadow. All rights reserved.</div>
</footer>

</body>
</html>
```